Prayer Service 12.28.2013

I need a flyer designed for a Christian prayer service. The title and theme is:
"Total and Complete Surrender for Total and Complete Deliverance!"
1. You have creative freedom with imagery and typography
2. I need a quick turnaround time
FLYER DETAILS:
A prayer, anointing, and deliverance all night prayer service, at Brightwater Assembly.
Saturday December 28 2013 from 9pm-6am.
Special guest speakers, prayer,anointing,and deliverance sessions.
For more information contact Sis Dorothy Whitfield at Brightwater Assembly 555 634 1297 Ext. 4816 or Monica Shaw at 555 802-3941

```html
<!DOCTYPE html>
<html lang="en">
<head>
<meta charset="utf-8">
<title>Total and Complete Surrender – All Night Prayer Service</title>
<link href="https://fonts.googleapis.com/css2?family=Rouge+Script&family=Cinzel:wght@600&display=swap" rel="stylesheet">
<style>
  :root {
    --frame-brown: #4a3312;
    --frame-yellow: #fde46a;
    --panel-orange: #fdb440;
    --title-maroon: #5c1616;
    --date-olive: #4c3a0e;
    --caps-brown: #3d2a0c;
    --photo-light: #d4c697;
    --photo-mid: #a8935f;
    --photo-dark: #4f4127;
  }
  * { margin: 0; padding: 0; box-sizing: border-box; }
  html, body { width: 733px; height: 1200px; overflow: hidden; background: var(--frame-brown); }
  .flyer { position: relative; width: 733px; height: 1200px; background: var(--frame-brown); }
  .hero-photo {
    position: absolute; left: 0; top: 0; width: 733px; height: 572px;
    background: radial-gradient(ellipse at 50% 45%, var(--photo-light) 0%, var(--photo-mid) 45%, var(--photo-dark) 100%);
  }
  .info-frame {
    position: absolute; left: 13px; top: 586px; width: 707px; height: 599px;
    background: var(--frame-yellow);
  }
  .info-panel {
    position: absolute; left: 26px; top: 599px; width: 683px; height: 575px;
    background: var(--panel-orange);
  }
  .line { position: absolute; white-space: nowrap; line-height: 1; }
  .script { font-family: "Rouge Script", cursive; }
  .caps { font-family: "Cinzel", serif; font-weight: 600; color: var(--caps-brown); }
  .title { color: var(--title-maroon); font-size: 50px; }
  .title-1 { left: 32px; top: 618px; }
  .title-2 { left: 80px; top: 677px; }
  .subtitle { font-size: 19px; letter-spacing: 4px; }
  .subtitle-1 { left: 134px; top: 748px; }
  .subtitle-2 { left: 0; width: 733px; text-align: center; top: 790px; }
  .service { left: 76px; top: 836px; font-size: 25px; letter-spacing: 5px; }
  .date { color: var(--date-olive); font-size: 50px; }
  .date-1 { left: 48px; top: 870px; }
  .date-2 { left: 0; width: 733px; text-align: center; top: 925px; }
  .speakers { left: 66px; top: 1030px; font-size: 24px; letter-spacing: 5px; }
  .sessions { font-size: 17px; letter-spacing: 4px; }
  .sessions-1 { left: 66px; top: 1072px; }
  .sessions-2 { left: 308px; top: 1104px; }
</style>
</head>
<body>
<main class="flyer">
  <div class="hero-photo" role="img" aria-label="Sepia photograph of several children's hands pressed together in prayer"></div>
  <div class="info-frame"></div>
  <div class="info-panel"></div>

  <h1 class="line script title title-1">Total and Complete Surrender for</h1>
  <p class="line script title title-2">Total and Complete Deliverance!</p>

  <p class="line caps subtitle subtitle-1">A prayer, anointing, and</p>
  <p class="line caps subtitle subtitle-2">deliverance</p>
  <p class="line caps service">ALL NIGHT PRAYER SERVICE.</p>

  <p class="line script date date-1">Saturday December 28 2013 from</p>
  <p class="line script date date-2">9pm-6am.</p>

  <p class="line caps speakers">SPECIAL GUEST SPEAKERS,</p>
  <p class="line caps sessions sessions-1">prayer,anointing,and</p>
  <p class="line caps sessions sessions-2">deliverance sessions.</p>
</main>
</body>
</html>
```